design a business card for a small company

Please design a business card with a black background. I have included a sample design, and you can try to emulate this. However, the logo should have different colors. Look at the picture [login to view URL]: the logo should have two colors as in this example. The VEK part should have the color of aluminium and the 842 AS part should have the color of stainless steel. Feel free to experiment.

Please use a high-def logo for your design.

The cards should be set up for the following text:

Name
Job title
Email address
Phone number
Company Name
Company address

Remember to create both front and back designs!

```html
<!DOCTYPE html>
<html lang="en">
<head>
<meta charset="utf-8">
<title>VEK 842 AS – Business Card</title>
<link rel="stylesheet" href="https://fonts.googleapis.com/css2?family=Source+Sans+3:wght@400;600&display=swap">
<style>
  :root {
    --backdrop: #58585a;
    --card-black: #000000;
    --gold-dark: #b07f3c;
    --gold-mid: #d9be7a;
    --gold-light: #fbf3cf;
    --gold-text: #f1dea3;
    --steel: #d6d8da;
    --white: #ffffff;
  }
  * { margin: 0; padding: 0; box-sizing: border-box; }
  html, body {
    width: 1104px; height: 1200px; overflow: hidden;
    background: var(--backdrop);
    font-family: "Source Sans 3", sans-serif;
  }
  .canvas { position: relative; width: 1104px; height: 1200px; }

  .card {
    position: absolute; left: 218px; width: 666px; height: 399px;
    background: var(--card-black); overflow: hidden;
  }
  .card--front { top: 178px; }
  .card--back { top: 622px; }

  .front-panel { position: absolute; left: 0; top: 0; width: 340px; height: 399px; }

  .brand-name {
    position: absolute; white-space: nowrap;
    font-family: "Source Sans 3", sans-serif; font-weight: 600;
    transform: translate(-50%, -50%);
    letter-spacing: 1px;
  }
  .brand-name--front { left: 150px; top: 180px; font-size: 44px; color: #1a1206; }
  .brand-name--back { left: 333px; top: 160px; font-size: 78px; color: var(--steel); }

  .contact { position: absolute; left: 353px; top: 0; color: var(--white); }
  .contact__name {
    position: absolute; left: 3px; top: 70px; white-space: nowrap;
    font-size: 37px; line-height: 1; font-weight: 400; color: var(--gold-text);
  }
  .contact__title {
    position: absolute; left: 3px; top: 110px; font-size: 19px; line-height: 1; white-space: nowrap;
  }
  .contact__row {
    position: absolute; left: 0; display: flex; align-items: flex-start;
    font-size: 22px; line-height: 30px; white-space: nowrap;
  }
  .contact__row svg { width: 22px; height: 22px; margin: 4px 14px 0 0; flex: none; }
  .contact__row--phone { top: 184px; }
  .contact__row--email { top: 229px; }
  .contact__row--address { top: 273px; }

  .back-band { position: absolute; left: 0; bottom: 0; width: 666px; height: 60px; }
</style>
</head>
<body>
<main class="canvas">

  <section class="card card--front" aria-label="Card front">
    <svg class="front-panel" viewBox="0 0 340 399" aria-hidden="true">
      <defs>
        <linearGradient id="goldSheen" x1="0" y1="0" x2="1" y2="0">
          <stop offset="0" stop-color="#a87a3a"/>
          <stop offset="0.22" stop-color="#e6cf8e"/>
          <stop offset="0.48" stop-color="#fdf7d8"/>
          <stop offset="0.75" stop-color="#d8bc78"/>
          <stop offset="1" stop-color="#b58843"/>
        </linearGradient>
      </defs>
      <polygon points="0,0 235,0 310,199 235,399 0,399" fill="url(#goldSheen)"/>
      <polyline points="243,0 318,199 243,399" fill="none" stroke="url(#goldSheen)" stroke-width="2.5"/>
      <polyline points="251,0 326,199 251,399" fill="none" stroke="url(#goldSheen)" stroke-width="2.5"/>
    </svg>
    <div class="brand-name brand-name--front">VEK 842 AS</div>

    <div class="contact">
      <p class="contact__name">Lars Holm</p>
      <p class="contact__title">owner</p>
      <p class="contact__row contact__row--phone">
        <svg viewBox="0 0 24 24" aria-hidden="true"><path fill="#f1dea3" d="M6.6 2.5l3 3.6-2 2.4c1.2 2.9 3.4 5.1 6.2 6.5l2.4-2 3.6 3-1.6 3.3c-.4.8-1.3 1.1-2.1.9C9.3 18.4 5.3 14.3 3.5 7.5c-.2-.8.2-1.7.9-2.1z"/></svg>
        555 0142 786
      </p>
      <p class="contact__row contact__row--email">
        <svg viewBox="0 0 24 24" aria-hidden="true"><rect x="2" y="5" width="20" height="14" fill="#f1dea3"/><polyline points="2,5 12,13 22,5" fill="none" stroke="#000" stroke-width="1.6"/></svg>
        larsholm@vekmail.com
      </p>
      <p class="contact__row contact__row--address">
        <svg viewBox="0 0 24 24" aria-hidden="true"><path fill="#f1dea3" d="M12 2a7 7 0 0 0-7 7c0 5 7 13 7 13s7-8 7-13a7 7 0 0 0-7-7zm0 9.5A2.5 2.5 0 1 1 12 6.5a2.5 2.5 0 0 1 0 5z"/></svg>
        <span>company name<br>company address here</span>
      </p>
    </div>
  </section>

  <section class="card card--back" aria-label="Card back">
    <div class="brand-name brand-name--back">VEK 842 AS</div>
    <svg class="back-band" viewBox="0 0 666 60" preserveAspectRatio="none" aria-hidden="true">
      <defs>
        <linearGradient id="bandSheen" x1="0" y1="0" x2="1" y2="0">
          <stop offset="0" stop-color="#b07f3c"/>
          <stop offset="0.2" stop-color="#e8d39a"/>
          <stop offset="0.45" stop-color="#fdf6d6"/>
          <stop offset="0.7" stop-color="#f2e2ac"/>
          <stop offset="1" stop-color="#b58641"/>
        </linearGradient>
      </defs>
      <polygon points="0,21 333,2 666,21 666,60 0,60" fill="url(#bandSheen)"/>
    </svg>
  </section>

</main>
</body>
</html>
```